Wattle Glen Manor Brochure Design

We need a brochure designed for our Aged Care Facility. We need designs that portray warmth and welcoming and at the same time something professional. We have attached the previous brochure and are looking for a modern professional brochure. We are not set on sizing and welcome ideas.

Attachments:
- One more high res photo is available via this link: https://www.filevaultex.net/s/kq52wpx9trmbe3n/Manor_High-Res_18.jpg?dl=0
- Another high res file has been added and is available through this link:
https://www.filevaultex.net/s/mv71cnd8yhsue6r/Manor_High-Res_24.jpg?dl=0

Target Market(s)

Aged Care and families

Requirements
Must have
• Logo and contact details

```html
<!DOCTYPE html>
<html lang="en">
<head>
<meta charset="utf-8">
<title>Wattle Glen Manor – Bi-fold Brochure</title>
<link href="https://fonts.googleapis.com/css2?family=Lato:wght@400;700;900&display=swap" rel="stylesheet">
<style>
  :root{
    --teal:#1f6f87;
    --teal-glass:rgba(24,104,128,.9);
    --navy:#1c4a6a;
    --slate:#5d7887;
    --paper:#ffffff;
    --bg:#e9eaec;
    --ink:#1d2b36;
  }
  *{box-sizing:border-box;margin:0;padding:0}
  html,body{width:1200px;height:1200px;overflow:hidden}
  body{background:var(--bg);font-family:"Lato",sans-serif;color:var(--ink);position:relative}
  .spread{position:absolute;left:210px;width:780px;height:551px;background:var(--paper);display:flex;box-shadow:0 8px 24px rgba(0,0,0,.18)}
  .spread--outside{top:32px}
  .spread--inside{top:617px}
  .panel{position:relative;width:390px;height:551px;overflow:hidden}
  .panel + .panel{border-left:1px solid #e2e4e6}
  .photo{position:absolute}
  .brand{display:flex;align-items:center;gap:6px;color:var(--slate);font-weight:700;letter-spacing:.06em;text-transform:uppercase}
  .brand__dot{width:12px;height:12px;border-radius:50%;background:var(--slate);flex:none}

  /* back panel */
  .back__photo{left:0;top:40px;width:390px;height:395px;background:linear-gradient(135deg,#eef0ef 0%,#d9ddd9 45%,#9fb39a 75%,#4f7a3e 100%)}
  .back__statement{position:absolute;left:55px;top:86px;width:225px;background:var(--teal-glass);color:#fff;font-weight:700;font-size:15.5px;line-height:1.28;text-align:center;padding:12px 10px}
  .back__footer{position:absolute;left:0;top:435px;width:390px;height:116px;display:flex;align-items:center;gap:18px;padding:0 20px}
  .back__logo .brand{font-size:12px}
  .contact{font-size:9.5px;line-height:1.3;color:var(--ink);font-style:normal}
  .contact__name{color:var(--navy);font-weight:900;font-size:11px}
  .contact__phone{display:flex;align-items:center;gap:4px}

  /* front panel */
  .front__logo{position:absolute;top:26px;left:0;width:390px;display:flex;justify-content:center}
  .front__logo .brand{font-size:14px}
  .front__photo{left:0;top:74px;width:390px;height:330px;background:linear-gradient(180deg,#3b7fd0 0%,#8ab8e4 28%,#5c8a4a 42%,#c9b07a 55%,#6fcde8 70%,#a8e2f2 100%)}
  .front__promise{position:absolute;top:432px;left:0;width:390px;text-align:center;color:var(--navy);font-weight:700;font-size:10.5px;line-height:1.35}
  .front__url{position:absolute;top:476px;left:0;width:390px;text-align:center;font-size:11px;letter-spacing:.32em;font-weight:700;color:var(--ink)}

  /* inside left */
  .needs__photo{inset:0;width:390px;height:551px;background:linear-gradient(180deg,#f4f4f2 0%,#e6e6e3 45%,#cfcfcc 60%,#2c2c2e 78%,#151517 100%)}
  .needs{position:absolute;left:40px;top:30px;width:330px;background:var(--teal-glass);color:#fff;padding:10px 14px 12px}
  .needs h2,.provides h2{font-weight:900;font-size:18px;letter-spacing:.01em;text-transform:uppercase}
  .checklist{list-style:none}
  .checklist li{position:relative;padding-left:14px;font-size:11.5px;line-height:1.25;font-weight:700}
  .checklist li::before{content:"✓";position:absolute;left:0;top:0}

  /* inside right */
  .provides{position:absolute;left:26px;top:26px;width:345px;color:var(--ink)}
  .provides h2{color:var(--navy);line-height:1.05;margin-bottom:6px}
  .provides .checklist li{font-size:11px;font-weight:700;line-height:1.22}
  .provides__photo{left:26px;top:395px;width:340px;height:135px;background:linear-gradient(180deg,#6d9fd4 0%,#b9d3ea 35%,#6a8a55 55%,#b8b6b0 75%,#8f8d88 100%)}
</style>
</head>
<body>

<section class="spread spread--outside" aria-label="Brochure outside spread">
  <div class="panel back">
    <div class="photo back__photo" role="img" aria-label="Photo of the bright foyer with lounge chair opening onto a lawn courtyard with outdoor table"></div>
    <p class="back__statement">Wattle Glen Manor is an accredited Government funded place... ...Aged care facility offering quality dignity and individuality for residents and their loved ones.</p>
    <div class="back__footer">
      <div class="back__logo">
        <span class="brand"><span class="brand__dot"></span>Wattle Glen Manor</span>
      </div>
      <address class="contact">
        <div class="contact__name">Wattle Glen Manor</div>
        18 Banksia Way<br>(Off Glenview Blvd)<br>Marlow Grove QLD 4100
        <div class="contact__phone">
          <svg width="9" height="9" viewBox="0 0 24 24" aria-hidden="true"><path fill="#1c4a6a" d="M6.6 10.8a15 15 0 0 0 6.6 6.6l2.2-2.2a1 1 0 0 1 1-.25 11.4 11.4 0 0 0 3.6.57 1 1 0 0 1 1 1V20a1 1 0 0 1-1 1A17 17 0 0 1 3 4a1 1 0 0 1 1-1h3.5a1 1 0 0 1 1 1c0 1.25.2 2.45.57 3.6a1 1 0 0 1-.25 1z"/></svg>
          07 5550 1234
        </div>
        www.wattleglenmanor.com.au
      </address>
    </div>
  </div>

  <div class="panel front">
    <div class="front__logo">
      <span class="brand"><span class="brand__dot"></span>Wattle Glen Manor</span>
    </div>
    <div class="photo front__photo" role="img" aria-label="Photo of the resort-style pool with palm trees and a single-storey villa"></div>
    <p class="front__promise">At Wattle Glen Manor, We're committed to your care and comfort.<br>Providing aged care with quality, dignity and individuality.</p>
    <p class="front__url">www.wattleglenmanor.com.au</p>
  </div>
</section>

<section class="spread spread--inside" aria-label="Brochure inside spread">
  <div class="panel">
    <div class="photo needs__photo" role="img" aria-label="Photo of a modern lounge with white sofas, red cushions and glossy black floor"></div>
    <div class="needs">
      <h2>If you need</h2>
      <ul class="checklist">
        <li>Low level or high level respite care</li>
        <li>Permanent Care</li>
        <li>Differing levels of care for you and your spouse together</li>
        <li>Specific dementia care and expertise</li>
        <li>Experienced and caring staff</li>
        <li>High quality accommodation and facilities</li>
        <li>A home where your family are welcomed</li>
        <li>Day care Dementia</li>
      </ul>
    </div>
  </div>

  <div class="panel">
    <div class="provides">
      <h2>Wattle Glen Manor<br>provides</h2>
      <ul class="checklist">
        <li>Large spacious rooms with ensuites</li>
        <li>A specialised dementia section</li>
        <li>Extensive kitchen, laundry and staff facilities</li>
        <li>Care for couples with differing levels of care so they can remain together</li>
        <li>Qualified and experienced nursing staff</li>
        <li>Divisional Therapists</li>
        <li>Home theatre room</li>
        <li>Hairdressing salon on site</li>
        <li>Doctor and therapist consulting rooms</li>
        <li>Spacious dining room</li>
        <li>Open lounges with library, internet, fireplace and recreation</li>
        <li>Tranquil leafy outdoor areas and indoor garden courtyard including BBQ and picnic grounds</li>
        <li>Common areas to enjoy and entertain visitors</li>
        <li>Specialised dementia wellness program as designed by Harlan Ostby (Don)</li>
      </ul>
    </div>
    <div class="photo provides__photo" role="img" aria-label="Photo of the paved garden walkway beside the residential wing under blue sky"></div>
  </div>
</section>

</body>
</html>
```